Design a business card
Business name: Larkspur Yield Advisory
Improving Business Profitibility

- An Overview of the Business & Service:

Business Performance Consulting

- The Target Market: Small to medium-sized business

- Design Specifics:
White card, blue ink, moon eclipse

No Logo

Target Market(s)

Small to medium-sized business

Font styles to use
Sans Serif

```html
<!DOCTYPE html>
<html lang="en">
<head>
<meta charset="utf-8">
<title>Larkspur Yield Advisory – Business Card</title>
<link href="https://fonts.googleapis.com/css2?family=Montserrat:wght@600&family=Lato:wght@400;700&display=swap" rel="stylesheet">
<style>
  :root {
    --page-bg: #ecebe8;
    --navy-top: #2f5585;
    --navy-bottom: #1a3866;
    --teal: #1596a8;
    --card-white: #f7f7f7;
    --ink-blue: #1f3f77;
    --ink-dark: #1e1e24;
  }
  * { margin: 0; padding: 0; box-sizing: border-box; }
  html, body { width: 1200px; height: 1200px; overflow: hidden; }
  body {
    background: var(--page-bg);
    display: flex;
    align-items: center;
    justify-content: center;
  }
  .business-card {
    width: 900px;
    height: 514px;
    display: flex;
    background: var(--card-white);
    box-shadow: 0 14px 40px rgba(0,0,0,0.14);
  }
  .brand-panel {
    width: 404px;
    background: linear-gradient(160deg, var(--navy-top), var(--navy-bottom));
    border-right: 7px solid var(--teal);
    display: flex;
    align-items: center;
    padding-left: 58px;
  }
  .brand-name {
    font-family: "Montserrat", sans-serif;
    font-weight: 600;
    font-size: 42px;
    line-height: 1.12;
    color: #ffffff;
  }
  .brand-name span { display: block; }
  .brand-name span:nth-child(2) { padding-left: 20px; }
  .brand-name span:nth-child(3) { padding-left: 40px; }
  .contact-panel {
    flex: 1;
    padding: 48px 44px 0 0;
    display: flex;
    flex-direction: column;
    align-items: flex-end;
    text-align: right;
  }
  .person-name {
    font-family: "Lato", sans-serif;
    font-weight: 700;
    font-size: 36px;
    line-height: 1.1;
    letter-spacing: 0.5px;
    color: var(--ink-blue);
  }
  .title-row {
    display: flex;
    align-items: flex-end;
    gap: 6px;
    margin-top: 4px;
  }
  .title-rule {
    width: 180px;
    height: 2px;
    background: var(--ink-dark);
    margin-bottom: 2px;
  }
  .person-title {
    font-family: "Lato", sans-serif;
    font-size: 12px;
    line-height: 1;
    letter-spacing: 0.8px;
    color: var(--ink-blue);
  }
  .address {
    font-family: "Lato", sans-serif;
    font-size: 22px;
    line-height: 1.25;
    color: var(--ink-blue);
    margin-top: 18px;
  }
  .contact-list {
    list-style: none;
    margin-top: 62px;
    font-family: "Lato", sans-serif;
    font-size: 25px;
    line-height: 1.32;
    color: var(--ink-dark);
  }
  .contact-list li {
    display: flex;
    align-items: center;
    justify-content: flex-end;
    gap: 10px;
  }
  .contact-icon { width: 20px; height: 20px; flex-shrink: 0; }
</style>
</head>
<body>
  <div class="business-card">
    <section class="brand-panel">
      <h1 class="brand-name">
        <span>Larkspur</span>
        <span>Yield</span>
        <span>Advisory</span>
      </h1>
    </section>
    <section class="contact-panel">
      <h2 class="person-name">NORA ELLERY</h2>
      <div class="title-row">
        <div class="title-rule"></div>
        <p class="person-title">FOUNDER &amp; CEO</p>
      </div>
      <p class="address">48 Alder Lane<br>Brookfield, OH, 44403</p>
      <ul class="contact-list">
        <li>(800) 555 0147
          <svg class="contact-icon" viewBox="0 0 20 20" aria-hidden="true">
            <circle cx="10" cy="10" r="8.5" fill="none" stroke="#1f3f77" stroke-width="1.6"/>
            <path d="M7 5.5l1.6 2.4-1 1c.6 1.3 1.6 2.3 2.9 2.9l1-1 2.4 1.6-.8 1.6c-3.6-.2-6.6-3.2-6.8-6.8z" fill="#1f3f77"/>
          </svg>
        </li>
        <li>hello@larkspuryield.com
          <svg class="contact-icon" viewBox="0 0 20 20" aria-hidden="true">
            <circle cx="10" cy="10" r="8.5" fill="none" stroke="#1f3f77" stroke-width="1.6"/>
            <rect x="5.5" y="7" width="9" height="6.5" fill="#1f3f77"/>
            <path d="M5.5 7l4.5 3.4L14.5 7" fill="none" stroke="#ffffff" stroke-width="1"/>
          </svg>
        </li>
        <li>www.larkspuryield.com
          <svg class="contact-icon" viewBox="0 0 20 20" aria-hidden="true">
            <circle cx="10" cy="10" r="8.5" fill="none" stroke="#1f3f77" stroke-width="1.6"/>
            <circle cx="10" cy="10" r="5" fill="none" stroke="#1f3f77" stroke-width="1.2"/>
            <path d="M5 10h10M10 5c-2 3-2 7 0 10M10 5c2 3 2 7 0 10" fill="none" stroke="#1f3f77" stroke-width="1"/>
          </svg>
        </li>
      </ul>
    </section>
  </div>
</body>
</html>
```